Executive Summary - Soccer Facility

We need help creating an Executive Summary 4 page template (A3 size print measuring 29.7 x 42.0cm, 11.69 x 16.53 inches) for our indoor soccer facility business plan. Our colors are black and white with yellow accents. Can also use soccer turf green where needed.
A design we like can be found here - https://flipreel.example/brightforgelab/docs/marlowe-exec-summary-designed_c517838225793d?e=0
We have the following sections;
Introduction, The Opportunity, The Facility, Projections, Who We Are, What We Need - How We'll Use It, Investor ROI.
We have some charts that need adding too of which we will work with the winning entry. This is when we will provide approved text to drop into the template.
30 - 40 year old professionals that play recreational soccer on weekends
- Molot (logo text)

```html
<!DOCTYPE html>
<html lang="en">
<head>
<meta charset="utf-8">
<title>Northgate Urban Soccer – Executive Summary</title>
<link href="https://fonts.googleapis.com/css2?family=Anton&family=Exo+2:wght@200;300;400;500;600&display=swap" rel="stylesheet">
<style>
:root{
  --yellow:#f2e922;
  --black:#0c0c0c;
  --white:#ffffff;
  --stage:#dcdcdc;
  --ink:#1e1e1e;
  --muted:#555;
  --turf:#3cb54a;
  --orange:#f26522;
  --sky:#29b6e8;
  --teal:#59c7b0;
  --pink:#f49ac1;
  --pale:#f7f39a;
  --ghost:rgba(255,255,255,.55);
}
*{box-sizing:border-box;margin:0;padding:0}
html,body{width:1200px;height:1200px;overflow:hidden;background:var(--stage)}
body{font-family:"Exo 2",sans-serif;color:var(--ink);position:relative}
.spread{position:absolute;left:200px;width:800px;height:565px;overflow:hidden;box-shadow:0 6px 18px rgba(0,0,0,.18)}
.spread--outer{top:15px;background:var(--yellow)}
.spread--inner{top:610px;background:var(--yellow)}
.abs{position:absolute}
.fold{position:absolute;top:0;bottom:0;width:1px;background:rgba(0,0,0,.12)}
.hl{background:var(--yellow);padding:0 3px;display:inline-block;line-height:1}
.heading{font-weight:400;text-transform:uppercase;color:var(--black);letter-spacing:.5px}
.body{font-size:6.4px;line-height:1.45;color:var(--ink);font-weight:400}
.ghost{position:absolute;color:var(--ghost);font-weight:200;font-family:"Exo 2",sans-serif;line-height:1;pointer-events:none}

/* back cover */
.data-panel{left:29px;top:37px;width:334px;height:498px;background:var(--white);border:3px solid var(--black)}
.sales-title{left:12px;top:14px;font-size:15px}
.sales-sub{left:12px;top:39px;width:160px;text-align:center;font-size:5.5px;line-height:1.3;text-transform:uppercase}
.pie-legend{left:8px;top:66px;font-size:4px;line-height:10px}
.pie-legend span{display:block}
.pie{left:84px;top:60px}
.pie-keys{left:8px;top:155px;width:176px;font-size:3.8px;display:flex;flex-wrap:wrap;gap:2px 6px}
.pie-keys i{display:inline-block;width:4px;height:4px;border-radius:50%;margin-right:2px;vertical-align:middle}
.proj-title{left:10px;top:188px;font-size:15px}
.proj-block{left:10px;top:213px;width:170px}
.proj-block h4{font-size:7px;font-weight:500;margin-bottom:2px}
.proj-block ul{list-style:none}
.proj-block li::before{content:"• "}
.fin-title{left:10px;top:281px;font-size:7px;font-weight:500}
.fin-table{left:7px;top:292px;width:180px;border-collapse:collapse;font-size:3.8px}
.fin-table th{background:var(--black);color:var(--white);font-weight:400;padding:2px 1px;text-align:center;border:1px solid var(--white)}
.fin-table th.now{background:var(--yellow);color:var(--black)}
.fin-table td{background:#e6e6e6;padding:2.5px 2px;border:1px solid var(--white);text-align:center}
.fin-table td:first-child{text-align:left;background:#cfcfcf}
.need-label{left:183px;top:14px;width:14px;height:250px}
.need-label span{position:absolute;left:0;top:0;transform-origin:0 0;transform:translate(13px,0) rotate(90deg);white-space:nowrap;font-size:10.5px;background:var(--yellow);padding:1px 3px;letter-spacing:.3px}
.need-copy{left:197px;top:6px;width:125px}
.need-copy p{margin-bottom:6px}
.need-copy ul{list-style:none}
.need-copy li{padding-left:6px;text-indent:-5px}
.need-copy li::before{content:"• "}
.roi-title{left:8px;top:354px;font-size:12px}
.roi-copy{left:8px;top:373px;width:78px}
.who-box{left:118px;top:345px;width:216px;height:153px;background:var(--black);clip-path:polygon(32px 0,100% 0,100% 100%,0 100%)}
.who-title{left:42px;top:12px;font-size:11.5px;color:var(--white)}
.who-copy{left:38px;top:29px;width:170px;color:var(--white);font-size:5.6px;line-height:1.45;text-align:center;font-weight:300}

/* front cover */
.cover{left:437px;top:0;width:332px;height:565px;background:var(--black)}
.cover-url{left:437px;top:32px;width:332px;text-align:center;color:var(--white);font-size:12px;letter-spacing:.6px}
.title-band{left:400px;top:56px;width:400px;height:108px;background:var(--yellow)}
.title-box{left:415px;top:69px;width:370px;height:80px;border:2px solid var(--black);display:flex;align-items:center;justify-content:center;overflow:hidden}
.title-box h1{font-family:"Anton",sans-serif;font-weight:400;font-size:32px;line-height:1;white-space:nowrap;color:var(--black);letter-spacing:0}
.quote{left:460px;top:180px;color:var(--white);font-size:32px;font-weight:200;line-height:35px}
.brand-mark{left:640px;top:322px;color:var(--white);font-family:"Anton",sans-serif;font-size:21px;letter-spacing:.5px;display:flex;align-items:center;gap:6px}
.brand-mark b{display:inline-block;width:9px;height:9px;background:var(--white)}
.intro-tab{left:400px;top:390px;width:188px;height:33px;background:var(--yellow);display:flex;align-items:center;padding-left:48px;font-size:14px;letter-spacing:.6px}
.intro-copy{left:452px;top:441px;width:160px;color:var(--white);font-size:9.5px;line-height:1.38;font-weight:300}
.phone-shot{left:618px;top:370px;width:182px;height:195px;border-radius:70px 0 0 0;background:linear-gradient(150deg,#e9e9e9 0%,#bdbdbd 45%,#8a7a6c 100%)}
.who-spill{left:337px;top:385px;font-size:52px}

/* inside spread */
.exec-panel{left:15px;top:15px;width:377px;height:127px;background:var(--white)}
.exec-title{left:0;top:12px;width:100%;text-align:center;font-size:17px}
.exec-col{top:44px;width:165px}
.exec-col--a{left:13px}
.exec-col--b{left:196px}
.exec-col{font-size:7.6px;line-height:1.45}
.opp-label{left:9px;top:176px;width:16px;height:178px}
.opp-label span{position:absolute;left:0;bottom:0;transform-origin:0 100%;transform:translate(14px,0) rotate(-90deg);white-space:nowrap;font-size:15px;letter-spacing:.4px;border-bottom:2px solid var(--white)}
.opp-copy{left:48px;top:170px;width:150px;font-size:7.6px;line-height:1.62}
.monitor{left:18px;top:390px;width:180px;height:104px;background:var(--black);padding:4px}
.monitor-screen{width:100%;height:100%;background:linear-gradient(180deg,#2d3b5c 0%,#3b3a4a 40%,#6d5f52 100%)}
.monitor-chin{left:18px;top:494px;width:180px;height:12px;background:#e4e4e4}
.monitor-neck{left:96px;top:506px;width:24px;height:20px;background:#cfcfcf;clip-path:polygon(20% 0,80% 0,100% 100%,0 100%)}
.monitor-foot{left:84px;top:525px;width:48px;height:3px;background:#bdbdbd;border-radius:2px}
.know-box{left:216px;top:142px;width:255px;height:73px;background:var(--black);clip-path:polygon(20px 0,100% 0,100% 100%,0 100%)}
.know-title{left:36px;top:8px;color:var(--white);font-size:15px;letter-spacing:.4px}
.know-copy{left:24px;top:29px;width:222px;color:var(--white);font-size:5.8px;text-align:center;font-weight:300}
.focus-copy{left:214px;top:224px;width:250px;font-size:7.6px;line-height:1.42}
.compare{left:214px;top:288px;width:250px;border-collapse:collapse;font-size:5.5px}
.compare th{background:var(--black);color:var(--white);font-weight:400;font-size:7px;line-height:1;padding:4px 2px;border:1px solid var(--yellow)}
.compare td{background:var(--white);border:2px solid var(--yellow);height:26.6px;padding:2px 5px;color:var(--muted);line-height:1.2}
.compare td.mark{text-align:center;width:81px}
.compare td.mark.wide{width:86px}
.xdot{display:inline-block;width:9px;height:9px;border-radius:50%;background:var(--black);color:var(--white);font-size:6px;line-height:9px;text-align:center}
.flex-band{left:198px;top:489px;width:405px;height:76px;background:var(--white);padding:6px 10px 0 10px;font-size:7.4px;line-height:1.42}
.facility-title{left:449px;top:19px;font-size:25px;background:var(--white);padding:0 3px;line-height:1}
.aerial-frame{left:487px;top:58px;width:279px;height:167px;border:2px solid var(--black)}
.aerial{left:493px;top:52px;width:273px;height:167px;background:linear-gradient(180deg,#c9d3db 0%,#8ea1ad 35%,#8a8b86 60%,#6d6a62 100%)}
.feature{display:flex;align-items:flex-start;gap:5px;font-size:7.4px;line-height:1.3;width:130px}
.feature svg{flex:0 0 auto}
.bm-title{left:487px;top:343px;font-size:23px;background:var(--white);padding:0 3px;line-height:1}
.core-line{left:489px;top:379px;font-size:12px;display:flex;align-items:center;gap:5px}
.pct{background:var(--black);color:var(--white);font-size:18px;padding:0 3px;line-height:1.1;border:1px solid var(--white)}
.rev-list{list-style:none;font-size:7.6px;line-height:12.4px}
.rev-list li::before{content:"• "}
.core-list{left:493px;top:401px}
.anc-pct{left:743px;top:436px}
.anc-title{left:631px;top:473px;font-size:12.5px}
.anc-list{left:633px;top:487px;line-height:12.2px}
</style>
</head>
<body>

<section class="spread spread--outer" aria-label="Outer spread">
  <div class="ghost" style="left:0;top:498px;font-size:48px">ROI</div>

  <div class="abs data-panel">
    <h2 class="abs heading sales-title"><span class="hl">Sales Forecast</span></h2>
    <p class="abs sales-sub">3 years cumulative sales<br>the importance of diversifying income</p>
    <div class="abs pie-legend" style="color:#999">
      <span style="color:#d8cf2a">Advertising: 9300 ●</span>
      <span style="color:#e7c83a">Merchandise: 12600 ●</span>
      <span style="color:var(--orange)">Concessions: 15300 ●</span>
      <span style="color:var(--pink)">Private Rentals: 22300 ●</span>
      <span style="color:var(--sky)">Youth Programs: 145000 ●</span>
      <span style="color:#e0a61c">Tournaments: 90000 ●</span>
      <span style="color:var(--orange)">Memberships: 207360 ●</span>
    </div>
    <svg class="abs pie" width="90" height="90" viewBox="-45 -45 90 90" role="img" aria-label="Pie chart of three-year cumulative sales by income stream">
      <g transform="rotate(-90)" fill="none" stroke-width="43">
        <circle r="21.5" stroke="#3cb54a" stroke-dasharray="74.3 135.1" stroke-dashoffset="0"/>
        <circle r="21.5" stroke="#f26522" stroke-dasharray="24.3 135.1" stroke-dashoffset="-74.3"/>
        <circle r="21.5" stroke="#f2e922" stroke-dasharray="10.8 135.1" stroke-dashoffset="-98.6"/>
        <circle r="21.5" stroke="#29b6e8" stroke-dasharray="8.1 135.1" stroke-dashoffset="-109.4"/>
        <circle r="21.5" stroke="#59c7b0" stroke-dasharray="6.8 135.1" stroke-dashoffset="-117.5"/>
        <circle r="21.5" stroke="#f49ac1" stroke-dasharray="5.4 135.1" stroke-dashoffset="-124.3"/>
        <circle r="21.5" stroke="#f7f39a" stroke-dasharray="5.4 135.1" stroke-dashoffset="-129.7"/>
      </g>
    </svg>
    <div class="abs pie-keys">
      <span><i style="background:var(--turf)"></i>Registrations</span>
      <span><i style="background:var(--orange)"></i>Memberships</span>
      <span><i style="background:var(--yellow)"></i>Tournaments</span>
      <span><i style="background:var(--sky)"></i>Youth Programs</span>
      <span><i style="background:var(--teal)"></i>Private Rentals</span>
      <span><i style="background:var(--orange)"></i>Concessions</span>
      <span><i style="background:var(--pale)"></i>Merchandise</span>
      <span><i style="background:var(--pink)"></i>Advertising</span>
    </div>

    <h2 class="abs heading proj-title"><span class="hl">Projections</span></h2>
    <div class="abs proj-block body" style="font-size:7px">
      <h4>PHYSICAL</h4>
      <ul>
        <li>Approximately 600,000 impressions<br>&nbsp;&nbsp;to I-5 northbound visitors weekly</li>
        <li>124 teams &amp; 1000+ players</li>
        <li>75,000 visitors per year and over<br>&nbsp;&nbsp;3500 unique visitors</li>
      </ul>
    </div>
    <h4 class="abs fin-title">FINANCIAL</h4>
    <table class="abs fin-table">
      <tr><th></th><th>2017<br>(60%)</th><th>2018<br>(75%)</th><th class="now">2019<br>(90%)</th><th>2019<br>(2 fields)</th><th>2020<br>(95%)</th><th>2021<br>(100%)</th></tr>
      <tr><td>Revenue</td><td>$481,846</td><td>$577,520</td><td>$683,394</td><td>$672,990</td><td>$725,302</td><td>$769,260</td></tr>
      <tr><td>Expense</td><td>$390,066</td><td>$378,775</td><td>$387,361</td><td>$418,574</td><td>$396,204</td><td>$405,282</td></tr>
      <tr><td>Net Profit</td><td>$91,780</td><td>$198,745</td><td>$295,833</td><td>$454,416</td><td>$329,098</td><td>$363,978</td></tr>
    </table>

    <div class="abs need-label"><span class="heading">What we need – How we'll use it</span></div>
    <div class="abs need-copy body">
      <p>Northgate Urban Soccer is currently seeking seed funding of $250,000 - $350,000 for stage I (launch phase) of their proposed National City facility.</p>
      <p>These funds will be spent on start-up expenses associated with site development including permitting, consultancy fees, building design and renovation, playing surface installation, off-field and online infrastructure, marketing and customer acquisition.</p>
      <p>The seed capital will be used over the first year of operations to reach the following business goals:</p>
      <ul>
        <li>Develop National City site and launch competitions</li>
        <li>Grow team patronage to 60% capacity</li>
        <li>Continue rolling out new features to build out from minimum viable product</li>
        <li>Build a unique brand and loyal following through key milestones and metrics</li>
        <li>Diversify income streams and increase ancillary income to 15%</li>
        <li>Test, tweak, and launch beta version of Northgate App</li>
        <li>Finalize a feasibility study into site purchase, a second field, and Series A funding round</li>
      </ul>
    </div>

    <h2 class="abs heading roi-title"><span class="hl">Investor ROI</span></h2>
    <p class="abs roi-copy body" style="font-size:6.3px">Quarterly investor updates and dividends will be distributed and paid to all investors with the annual return forecast to be between $1,500 - $3,500.</p>

    <div class="abs who-box">
      <h2 class="abs heading who-title" style="color:var(--white)">Who are we?</h2>
      <p class="abs who-copy">The strengths of Northgate Urban Soccer are intrinsically linked with the skills and experiences of its two founders. Having both played numerous forms of indoor soccer across different continents, running federation affiliated clubs and tournaments and participating in international soccer tournaments, Dale Morrow and Tomas Reyes have spent the past year researching and predicting the future trends of the indoor market. Together with over 30 years combined experience in fundraising, sales, civic engagement and event management from Federal Government through Fortune 500 companies, their partnership and innovative approach to the recreational side of the game are a strong value proposition for future investors.</p>
    </div>
  </div>

  <div class="fold" style="left:400px"></div>

  <div class="abs cover"></div>
  <div class="ghost who-spill">W</div>
  <p class="abs cover-url">www.northgateurbansoccer.example</p>
  <div class="abs title-band"></div>
  <div class="abs title-box"><h1>NORTHGATE URBAN SOCCER</h1></div>
  <p class="abs quote">“Its Football<br>But Not<br>As You<br>Know It.”</p>
  <div class="abs brand-mark"><b></b>NORTHGATE</div>
  <div class="abs intro-tab heading">Introduction</div>
  <p class="abs intro-copy">Indoor soccer in the U.S. is a near $1bn industry with no market leader and no clear identity on the broader sporting landscape. This lack of identity has led to a cookie cutter approach to facilities nationwide and a distinct lack of atmosphere at venues.</p>
  <div class="abs phone-shot" role="img" aria-label="Photo of a hand holding a smartphone showing the club app"></div>
</section>

<section class="spread spread--inner" aria-label="Inner spread">
  <div class="ghost" style="left:392px;top:48px;font-size:90px">ES</div>
  <div class="ghost" style="left:696px;top:-14px;font-size:90px">TF</div>
  <div class="ghost" style="left:700px;top:384px;font-size:62px">BM</div>
  <div class="ghost" style="left:5px;top:505px;font-size:70px">TO</div>

  <div class="abs exec-panel">
    <h2 class="abs heading exec-title"><span class="hl">Executive Summary</span></h2>
    <p class="abs exec-col exec-col--a">Northgate Urban Soccer is a California Corporation that owns and operates boutique indoor soccer facilities focused on quality across all facets of the player experience, innovative soccer technology and being a unique social hub of the communities of which they service.</p>
    <p class="abs exec-col exec-col--b">Our vision is to be the leading indoor soccer facility brand across the country. We aim to achieve this through our innovative approaches to the game and building a loyal and interconnected player network, culminating in a respected lifestyle brand.</p>
  </div>

  <div class="abs opp-label"><span class="heading">The Opportunity</span></div>
  <p class="abs opp-copy">Northgate Urban Soccer is much a lifestyle brand as it is an indoor soccer facility in that it understands and engages its patrons rather than perform the basic duties of a transactional entity that refuses to be flexible in a changing economy. Our research has shown that the market is ripe for a new type of indoor soccer facility, one that provides more personalization, connectivity and value to players and transforms venues into unique soccer hubs that players, supporters, friends, and families can come together and enjoy.</p>

  <div class="abs monitor"><div class="monitor-screen" role="img" aria-label="Video still of an indoor soccer match with highlight overlay"></div></div>
  <div class="abs monitor-chin"></div>
  <div class="abs monitor-neck"></div>
  <div class="abs monitor-foot"></div>

  <div class="abs know-box">
    <h2 class="abs heading know-title" style="color:var(--white)">Did you know?</h2>
    <p class="abs know-copy">The current indoor format was created due to North Americans' familiarity with hockey and the existence of hockey arenas, which then adapted their game for these facilities. A</p>
  </div>
  <p class="abs focus-copy">Northgate Urban Soccer's focus on combining an enhanced player experience with personalized technology (including an app, in-game video and packaged highlights) is a key differentiator in this market and will drive future growth.</p>

  <table class="abs compare">
    <tr><th>Services</th><th>Current Indoor<br>Soccer</th><th>Northgate Urban<br>Soccer</th></tr>
    <tr><td>Organized leagues</td><td class="mark"><span class="xdot">✕</span></td><td class="mark wide"><span class="xdot">✕</span></td></tr>
    <tr><td>App to connect with team and see latest live stats</td><td class="mark"></td><td class="mark wide"><span class="xdot">✕</span></td></tr>
    <tr><td>Team personalization – logos &amp; kits</td><td class="mark"></td><td class="mark wide"><span class="xdot">✕</span></td></tr>
    <tr><td>Video highlight packages</td><td class="mark"></td><td class="mark wide"><span class="xdot">✕</span></td></tr>
    <tr><td>Community engagement</td><td class="mark"></td><td class="mark wide"><span class="xdot">✕</span></td></tr>
    <tr><td>Weekend Finals &amp; Tournaments</td><td class="mark"></td><td class="mark wide"><span class="xdot">✕</span></td></tr>
  </table>

  <p class="abs flex-band">Flexibility and innovation is a necessity for success and carving out a niche in the market. Many indoor soccer venues are limited with their services due to the necessity of maximizing league participation in the evenings and leaving little time to appeal to larger (and more lucrative) junior markets. The fields are also often oversized and cannot serve multiple functions because they are contained within rigid, purpose-built walls.</p>

  <div class="fold" style="left:404px"></div>

  <h2 class="abs heading facility-title">The Facility</h2>
  <div class="abs aerial-frame"></div>
  <div class="abs aerial" role="img" aria-label="Aerial photo of the bay-front city district around the facility site"></div>

  <div class="abs feature" style="left:497px;top:236px">
    <svg width="11" height="11" viewBox="0 0 12 12"><circle cx="6" cy="6" r="6" fill="#0c0c0c"/><path d="M6 2.5V6l2.5 1.5" stroke="#fff" stroke-width="1.2" fill="none"/></svg>
    <span>5 minutes from downtown San Diego</span>
  </div>
  <div class="abs feature" style="left:497px;top:264px">
    <svg width="11" height="11" viewBox="0 0 12 12"><circle cx="6" cy="6" r="6" fill="#0c0c0c"/><rect x="3" y="3" width="6" height="6" fill="none" stroke="#fff" stroke-width="1.1"/></svg>
    <span>15,670 sq. ft.</span>
  </div>
  <div class="abs feature" style="left:497px;top:288px">
    <svg width="11" height="11" viewBox="0 0 12 12"><circle cx="6" cy="6" r="6" fill="#0c0c0c"/><path d="M6 2.5v7M4.5 2.5h3M4.5 9.5h3" stroke="#fff" stroke-width="1.1"/></svg>
    <span>Field is within regulation futsal dimension</span>
  </div>
  <div class="abs feature" style="left:633px;top:236px">
    <svg width="11" height="11" viewBox="0 0 12 12"><circle cx="6" cy="6" r="6" fill="#0c0c0c"/><path d="M3 9V4h6v5M4.5 5.5h1M6.5 5.5h1M4.5 7h1M6.5 7h1" stroke="#fff" stroke-width="1"/></svg>
    <span>2 story building with urban theme</span>
  </div>
  <div class="abs feature" style="left:633px;top:264px">
    <svg width="11" height="11" viewBox="0 0 12 12"><circle cx="6" cy="6" r="6" fill="#0c0c0c"/><rect x="3" y="4" width="6" height="4" fill="none" stroke="#fff" stroke-width="1"/></svg>
    <span>Electronic advertising hoarding</span>
  </div>
  <div class="abs feature" style="left:633px;top:292px">
    <svg width="11" height="11" viewBox="0 0 12 12"><circle cx="6" cy="6" r="6" fill="#0c0c0c"/><path d="M4.5 3.5L8.5 6l-4 2.5z" fill="#fff"/></svg>
    <span>Full video &amp; sound</span>
  </div>

  <h2 class="abs heading bm-title" style="background:var(--white)">Business Model</h2>
  <div class="abs core-line heading">Core revenue <span class="pct">80%</span></div>
  <ul class="abs rev-list core-list">
    <li>Competitive Soccer Leagues</li>
    <li>Youth Instructional programs</li>
    <li>Tournaments</li>
    <li>School programs</li>
    <li>Private Rentals</li>
    <li>Sponsorship &amp; advertising</li>
  </ul>
  <div class="abs anc-pct"><span class="pct">20%</span></div>
  <p class="abs heading anc-title">Ancillary revenue</p>
  <ul class="abs rev-list anc-list">
    <li>Retail &amp; equipment sales</li>
    <li>Memberships</li>
    <li>Niche partnerships</li>
    <li>Concessions</li>
    <li>Games zone/Classroom</li>
    <li>Community Events</li>
  </ul>
</section>

</body>
</html>
```